Rebuild

Hello,
I got a new logo, and a new business name. Now I need that new identity on a new web page.
Please take a look at my existing site. www.critterfixhub.com
and please build me a new website with my new logo and get it posted at my new domain www.tobymarlowcatching.com
Updates
Please include in the design the Radio marketing tagline "Toby Marlow, Raised and Made for Wildlife Control".
I would like to add that it is usually understood that I will capture and remove problem causing animals. However, what I really need to emphasize is that I fortify homes and other structures to keep the animals out long term. Trapping is a temporary solution. Home fortification such as reinforcing vent screens, sealing holes, and constructing secure barriers is the Permanent solution. Kind of like a home security system for vertebrate pests. You don't really need an alarm system if you have the best locks and steel doors.
Obviously, my website is a multiple page website. Some designs will be good for the home page, and others for secondary pages.
Ultimately, I need a good home page that will attract clients, and then good backup pages to explain the different aspects of my work.
I imagine a home page. Sub pages would include Home Fortifications, Species detail pages, Company history, FAQs, Odd and unusual services, specialties, and where to go for the things I don't do. The text for these pages is something I can write myself. I'm a good writer. Just not a very good visual artist.
I have added the logo in .eps, and I have also added the mirror image logo in both eps and jpg. Let me know if other formats are needed.
I've posted a bunch of photos on my facebook for perusal
http://www.facebook.com/pages/Toby-Marlow-Wildlife-Control/735218064391852
Target Market(s)
Upper to middle income homeowners
Industry/Entity Type
Business
Look and feel
Each slider illustrates characteristics of the customer's brand and the style your logo design should communicate.

```html
<!DOCTYPE html>
<html lang="en">
<head>
<meta charset="utf-8">
<title>Toby Marlow Wildlife Control</title>
<link rel="stylesheet" href="https://fonts.googleapis.com/css2?family=Arimo:ital,wght@0,400;0,700;1,400&display=swap">
<style>
:root{
  --orange:#f3ad40;
  --orange-light:#fbd27e;
  --orange-text:#e0922c;
  --brown:#3d3028;
  --brown-dark:#2f251f;
  --teal:#3e9db3;
  --teal-dark:#2b7f93;
  --beige:#ece0c8;
  --beige-light:#f6efe2;
  --side:#f3ebdc;
  --page:#fbf8f2;
  --text:#333;
  --white:#fff;
}
*{margin:0;padding:0;box-sizing:border-box}
html,body{width:1200px;height:2222px;overflow:hidden}
body{font-family:"Arimo",Arial,sans-serif;color:var(--text);background:var(--page);position:relative}
.header{position:absolute;top:0;left:0;width:1200px;height:136px;background:linear-gradient(var(--orange-light),var(--orange))}
.brand{position:absolute;left:44px;top:8px;display:flex;align-items:center}
.brand-mark{width:124px;height:124px;border-radius:50%;background:var(--brown);border:5px solid var(--white)}
.brand-text{margin-left:22px}
.brand-name{font-size:46px;font-weight:700;color:var(--brown);line-height:1}
.brand-tagline{font-size:23px;color:var(--brown);margin-top:6px}
.call{position:absolute;right:44px;top:52px;font-size:22px;font-weight:700;color:var(--brown)}
.call span{color:var(--teal-dark);font-size:30px;font-weight:400;margin-left:14px}
.nav{position:absolute;top:136px;left:0;width:1200px;height:74px;background:var(--brown)}
.nav ul{list-style:none;display:flex;position:absolute;left:42px;top:26px}
.nav li{font-size:19px;font-weight:700;color:var(--white);padding:0 14px;border-left:1px solid #6b5a4d;line-height:22px}
.nav li:first-child{padding-left:0;border-left:0;color:var(--teal)}
.social{position:absolute;right:42px;top:26px;display:flex;gap:18px;font-size:16px;color:var(--beige)}
.hero{position:absolute;top:210px;left:0;width:1200px;height:445px;background:var(--beige)}
.hero-panel{position:absolute;left:42px;top:49px;width:1116px;height:346px;background:var(--brown);border-radius:6px;overflow:hidden}
.offer{position:absolute;left:0;top:22px;width:560px;text-align:center}
.offer-title{font-size:52px;color:var(--teal);line-height:1.2}
.offer-deal{font-size:46px;color:var(--orange);line-height:1.15;margin-top:10px}
.offer-line{font-size:38px;color:var(--orange);line-height:1.25}
.hero-photo{position:absolute;z-index:2;left:657px;top:57px;width:395px;height:284px;background:linear-gradient(135deg,#8d8a7f,#4e4a42);border:6px solid #c7b08a}
.breadcrumb{position:absolute;z-index:1;left:0;bottom:0;width:100%;height:37px;background:var(--teal);color:var(--white);font-size:16px;line-height:37px;padding-left:36px}
.main{position:absolute;top:655px;left:0;width:1200px;height:1000px}
.content{position:absolute;left:44px;top:58px;width:648px;font-size:14.6px;line-height:20.5px}
.content h1{font-size:29px;font-weight:400;color:var(--brown-dark);line-height:1.1}
.date{font-size:13px;font-style:italic;font-weight:700;color:var(--orange-text);margin:4px 0 16px}
.content p{margin-bottom:20px;text-align:justify}
.inline-photo{float:right;width:290px;height:165px;margin:2px 0 8px 14px;background:linear-gradient(160deg,#6d8f9a,#3f5260);border:4px solid var(--orange)}
.btn{display:inline-block;background:linear-gradient(var(--orange-light),var(--orange));color:var(--white);font-weight:700;font-size:19px;padding:6px 16px;border-radius:3px}
.content .btn{float:right}
.sidebar{position:absolute;left:748px;top:60px;width:412px;padding-top:26px;padding-bottom:10px;background:linear-gradient(90deg,var(--side),rgba(243,235,220,0))}
.side-head{height:44px;background:linear-gradient(90deg,var(--orange),rgba(243,173,64,0));font-size:29px;font-weight:700;color:var(--brown-dark);padding:6px 0 0 46px}
.side-list{list-style:none;padding:12px 0 20px 60px}
.side-list li{font-size:18px;line-height:28px;position:relative;color:var(--brown-dark)}
.side-list li::before{content:"";position:absolute;left:-18px;top:12px;width:6px;height:6px;background:var(--brown-dark)}
.payments{position:absolute;left:32px;top:926px;display:flex;align-items:center;gap:16px;font-size:16px}
.card{width:64px;height:36px;border:1px solid #b8ae9e;border-radius:4px;background:var(--white);font-size:11px;font-weight:700;color:#555;display:flex;align-items:center;justify-content:center}
.footer{position:absolute;top:1655px;left:0;width:1200px;height:490px;background:var(--brown)}
.footer h2{font-size:30px;font-weight:400;color:var(--teal)}
.col-contact{position:absolute;left:40px;top:54px;width:320px}
.field{background:var(--beige-light);border:1px solid #c8b895;color:#8a7b63;font-size:14px;padding:10px 12px;height:42px}
.row{display:flex;gap:10px;margin-top:22px}
.row .field{width:135px}
.field.tall{height:130px;margin-top:8px;width:320px}
.field.area{margin-top:22px;width:320px}
.col-contact .btn{margin:22px 0 0 190px}
.col-assoc{position:absolute;left:450px;top:54px;width:320px}
.badges{position:relative;height:270px}
.badge{position:absolute;border-radius:50%}
.b1{left:0;top:30px;width:148px;height:148px;background:#ef9b2c;border:8px solid #c43a27}
.b2{left:180px;top:30px;width:148px;height:148px;background:#f2a638;border:8px solid #5a9f3a}
.b3{left:8px;top:195px;width:312px;height:80px;background:var(--orange);border:4px solid #f9d38a}
.col-assoc .btn{margin:30px 0 0 186px}
.col-test{position:absolute;left:852px;top:54px;width:310px}
.test{display:flex;margin-top:24px;height:44px}
.avatar{width:36px;height:36px;background:#c5ccd6;border:2px solid var(--white);margin-right:16px}
.test strong{display:block;font-size:15px;font-weight:400;color:var(--white)}
.test em{font-size:14px;color:var(--orange)}
.col-test .btn{margin:28px 0 0 180px}
.bottom{position:absolute;top:2145px;left:0;width:1200px;height:77px;background:var(--teal);color:var(--white);font-size:15px}
.bottom p{position:absolute;left:44px;top:30px}
.bottom ul{position:absolute;right:44px;top:30px;list-style:none;display:flex}
.bottom li{padding:0 6px;border-left:1px solid var(--white);line-height:15px}
.bottom li:first-child{border-left:0}
</style>
</head>
<body>
<header class="header">
  <div class="brand">
    <div class="brand-mark"></div>
    <div class="brand-text">
      <div class="brand-name">Toby Marlow</div>
      <div class="brand-tagline">Raised &amp; Made for Wildlife Control</div>
    </div>
  </div>
  <div class="call">Call Us Now:<span>360-555-0148</span></div>
</header>
<nav class="nav">
  <ul>
    <li>Home</li><li>About</li><li>Animal Control</li><li>Wildfire Services</li><li>Testimonials</li><li>Contact</li>
  </ul>
  <div class="social"><span>Folkly</span><span>Snapfeed</span><span>Chirper</span></div>
</nav>
<section class="hero">
  <div class="hero-panel">
    <div class="offer">
      <div class="offer-title">We Can Help!</div>
      <div class="offer-deal">10% Off</div>
      <div class="offer-line">initial service with</div>
      <div class="offer-line">purchase of repairs!</div>
    </div>
    <div class="hero-photo" role="img" aria-label="Photo of a raccoon inside a wire live trap"></div>
    <div class="breadcrumb">You're here : Home &gt; Welcome...</div>
  </div>
</section>
<main class="main">
  <article class="content">
    <h1>Animal Problems Gone. Permanent Solutions.</h1>
    <div class="date">September 20th 2012</div>
    <p><span class="inline-photo" role="img" aria-label="Photo of the owner standing beside an animal control sign"></span>If you are dealing with unwanted animals on your property in Thurston, Lewis, or Pierce Counties, Wildlife control services that you can count on are available. Call Toby Marlow Wildlife Control, I can take care of these nuisances for you, and you'll never have to deal with it again. I am THE experts that will come to your home to assess the problem and take care of it in a professional manner.</p>
    <p>If you are dealing with unwanted animals on your property in Thurston, Lewis, or Pierce Counties, Wildlife control services that you can count on are available. Call Toby Marlow Wildlife Control, I can take care of these nuisances for you, and you'll never have to deal with it again. I am THE experts that will come to your home to assess the problem and take care of it in a professional manner.</p>
    <p>I specialize in nuisance wildlife management, not insects or spiders. As a leader in providing these services for commercial, residential and industrial clients, I can get the job done right the first time so that you don't have to worry about it again. I have more extensive knowledge and training than any other operator in the Northwest, and have a lifelong passion about the wildlife specific to Western Washington. I will always take care of the problem in the most gentle and humane way possible.</p>
    <p>I am licensed, bonded, and insured as a contractor and comply with all Laws and Regulations set by the Departments of Fish and Wildlife, Labor and Industries, and Revenue to ensure your complete protection. I am a state certified trapper and an Expert marksman and can handle any pest problem you may have.</p>
    <p>For your property in Seattle, pest control experts can handle any animal removal that you need. Call Allpoint Animal Control today to have one of our experts to your home today!</p>
    <p>Wildwise Pest Control in Washington discusses bat removal, prevention and treatment of wildlife invasion in your home or other property.</p>
    <span class="btn">Read More</span>
  </article>
  <aside class="sidebar">
    <div class="side-head">Services</div>
    <ul class="side-list">
      <li>Animal Control</li><li>Bat Control</li><li>Opossum Control</li><li>Raccoon Control</li><li>Rat Control</li><li>Skunk Control</li><li>Squirrel Control</li><li>Starling Control</li><li>Otter Control</li>
    </ul>
    <div class="side-head">Why Choose Us?</div>
    <ul class="side-list">
      <li>PNU Wildlife Biologist</li><li>Certified Wildlife Professionals</li><li>State Certified Trappers</li><li>Certified Marksmen</li><li>Bonded, Licensed, and Insured Contractors</li><li>Humane Certified Professional Animal Control Expert</li><li>Former Military Police Game Warden</li><li>Wild Lands Conservation Group Member</li><li>Cascade Trappers Guild Members</li><li>Former Military Police Game Warden</li><li>Fort Alder Natural Resource Officer</li>
    </ul>
  </aside>
  <div class="payments">
    <span>Payment Methods:</span>
    <span class="card">Amberline</span><span class="card">Cash</span><span class="card">Corvex</span><span class="card">Check</span><span class="card">Mintcard</span><span class="card">Payway</span><span class="card">Vesta</span>
  </div>
</main>
<footer class="footer">
  <section class="col-contact">
    <h2>Contact Us</h2>
    <div class="row"><div class="field">Your name</div><div class="field">Your email</div></div>
    <div class="field tall">Your message</div>
    <div class="field area">Area</div>
    <span class="btn">SUBMIT</span>
  </section>
  <section class="col-assoc">
    <h2>Associations</h2>
    <div class="badges">
      <div class="badge b1" role="img" aria-label="Wildlife operators association badge"></div>
      <div class="badge b2" role="img" aria-label="Green business certification badge"></div>
      <div class="badge b3" role="img" aria-label="Service listing badge"></div>
    </div>
    <span class="btn">More</span>
  </section>
  <section class="col-test">
    <h2>Testimonials</h2>
    <div class="test"><div class="avatar"></div><div><strong>Dale</strong><em>"Very good service, Helpful and friendly."</em></div></div>
    <div class="test"><div class="avatar"></div><div><strong>Dale</strong><em>"Very good service, Helpful and friendly."</em></div></div>
    <div class="test"><div class="avatar"></div><div><strong>Dale</strong><em>"Very good service, Helpful and friendly."</em></div></div>
    <div class="test"><div class="avatar"></div><div><strong>Dale</strong><em>"Very good service, Helpful and friendly."</em></div></div>
    <span class="btn">Read More</span>
  </section>
</footer>
<div class="bottom">
  <p>Copyright ©2012 | Toby Marlow Catching | All rights reserved</p>
  <ul><li>Home</li><li>About</li><li>Services</li><li>Wildlife Control</li><li>Privacy Policy</li><li>Contact</li></ul>
</div>
</body>
</html>
```